Harvest of Kingdoms
preparing the way of the Lord...
Modern
Tom Farrel
412 Co.Rd. 118 Marlow, Pa.17602
tomjane4Faith@postvale.com
www.tf-harvestofkingdoms.com
preaching the gospel of Jesus, and teaching others to do the same.
mission trips
rallies and revivals
camps
this is for business cards and letterhead...

```html
<!DOCTYPE html>
<html lang="en">
<head>
<meta charset="utf-8">
<title>Harvest of Kingdoms – Business Card</title>
<link href="https://fonts.googleapis.com/css2?family=PT+Sans:wght@400;700&display=swap" rel="stylesheet">
<style>
  :root {
    --page-bg: #e9e7e2;
    --card-white: #ffffff;
    --green-light: #3aa14f;
    --green-dark: #17682d;
    --swoosh-blue: #1f5ea8;
    --ink: #1c1c1c;
    --on-green: #ffffff;
  }
  * { margin: 0; padding: 0; box-sizing: border-box; }
  html, body {
    width: 1200px; height: 799px; overflow: hidden;
    background: var(--page-bg);
    font-family: "PT Sans", Arial, sans-serif;
  }
  .canvas {
    position: relative; width: 1200px; height: 799px;
  }
  .business-card {
    position: absolute; left: 192px; top: 176px;
    width: 816px; height: 446px;
    border-radius: 30px; overflow: hidden;
    background: var(--card-white);
    box-shadow: 0 6px 18px rgba(0,0,0,0.18);
  }
  .card-shapes { position: absolute; inset: 0; }
  .brand {
    position: absolute; left: 0; right: 0; top: 92px;
    display: flex; justify-content: center; align-items: center; gap: 16px;
  }
  .brand-dot {
    width: 34px; height: 34px; border-radius: 50%;
    background: var(--swoosh-blue);
  }
  .brand-name {
    font-size: 58px; font-weight: 400; color: var(--ink);
    letter-spacing: 1px; line-height: 1;
  }
  .person {
    position: absolute; left: 118px; top: 326px; width: 220px;
    text-align: center; color: var(--on-green);
  }
  .person-name { font-size: 23px; font-weight: 700; line-height: 1.2; }
  .person-org { font-size: 17px; font-weight: 700; margin-top: 6px; }
  .divider {
    position: absolute; left: 396px; top: 283px;
    width: 1px; height: 144px; background: rgba(255,255,255,0.85);
  }
  .contact {
    position: absolute; left: 427px; top: 306px;
    list-style: none; color: var(--on-green);
    font-size: 16.5px; line-height: 28px;
  }
  .contact li { display: flex; align-items: center; gap: 10px; }
  .contact .address { padding-left: 0; }
  .contact svg { width: 13px; height: 13px; flex: none; }
</style>
</head>
<body>
<div class="canvas">
  <div class="business-card">
    <svg class="card-shapes" width="816" height="446" viewBox="0 0 816 446">
      <defs>
        <linearGradient id="greenFill" x1="0" y1="0" x2="0" y2="1">
          <stop offset="0" stop-color="var(--green-light)"/>
          <stop offset="1" stop-color="var(--green-dark)"/>
        </linearGradient>
      </defs>
      <path d="M0 170 Q408 372 816 170 L816 446 L0 446 Z" fill="url(#greenFill)"/>
      <path d="M0 170 Q408 372 816 170 L816 176 Q408 348 0 176 Z" fill="var(--swoosh-blue)"/>
      <path d="M0 160 Q408 352 816 160 L816 170 Q408 372 0 170 Z" fill="var(--swoosh-blue)"/>
    </svg>

    <div class="brand">
      <span class="brand-dot"></span>
      <span class="brand-name">Harvest of Kingdoms</span>
    </div>

    <div class="person">
      <div class="person-name">Tom Farrel</div>
      <div class="person-org">Harvest of Kingdoms</div>
    </div>

    <div class="divider"></div>

    <ul class="contact">
      <li class="address">412 Co.Rd. 118 Marlow, Pa.17602</li>
      <li>
        <svg viewBox="0 0 16 16"><path d="M4 1l3 3-2 2c1 2 3 4 5 5l2-2 3 3-2 3C7 15 1 9 1 3z" fill="#fff"/></svg>
        570.555.0142 (Toll Free)
      </li>
      <li>
        <svg viewBox="0 0 16 16"><rect x="1" y="3" width="14" height="10" fill="#fff"/><path d="M1 3l7 6 7-6" fill="none" stroke="#17682d" stroke-width="1.5"/></svg>
        tomjane4Faith@postvale.com
      </li>
      <li>
        <svg viewBox="0 0 16 16"><circle cx="8" cy="8" r="7" fill="#fff"/><path d="M1 8h14M8 1c-3 4-3 10 0 14M8 1c3 4 3 10 0 14" fill="none" stroke="#17682d" stroke-width="1"/></svg>
        www.tf-harvestofkingdoms.com
      </li>
    </ul>
  </div>
</div>
</body>
</html>
```